we are in the infrastructure business ( road construction ) and I need a billboard that I placed it at every project to illustrate that we worked there . We have the logo , I attached it , I just need an interesting design of the billboard.
The company s name is : Vextra Civil - I attached how to be written !
I don't need to write road construction business on it

Requirements
Must have
• Study the design of the logo I attached ( the sign with " KTP " is just an example !!
Nice to have
• the romanian flag but made into a special form ( I attached an Idea )

```html
<!DOCTYPE html>
<html lang="en">
<head>
<meta charset="utf-8">
<title>Vextra Civil – Project Billboard</title>
<link href="https://fonts.googleapis.com/css2?family=Barlow+Condensed:wght@700&display=swap" rel="stylesheet">
<style>
  :root {
    --page-bg: #f2f4f6;
    --panel-bg: #e7e8eb;
    --ink: #1f2e3d;
    --flag-blue: #1f3f99;
    --flag-yellow: #f1d23a;
    --flag-red: #df3140;
    --accent-sky: #4fb6df;
    --skyline-light: #e2e3e6;
    --skyline-mid: #c9cbcf;
    --silhouette: #3a3e44;
    --ground: #2a2d31;
  }
  * { margin: 0; padding: 0; box-sizing: border-box; }
  html, body {
    width: 1200px;
    height: 920px;
    overflow: hidden;
    background: var(--page-bg);
  }
  .billboard {
    position: absolute;
    left: 0;
    top: 176px;
    width: 1200px;
    height: 567px;
    background: var(--panel-bg);
    overflow: hidden;
  }
  .flag-band {
    display: flex;
    height: 29px;
  }
  .flag-band .stripe-blue { flex: 0 0 32.2%; background: var(--flag-blue); }
  .flag-band .stripe-yellow { flex: 0 0 35.2%; background: var(--flag-yellow); }
  .flag-band .stripe-red { flex: 1; background: var(--flag-red); }
  .wordmark {
    position: absolute;
    left: 0;
    top: 120px;
    width: 1200px;
    height: 260px;
  }
  .wordmark-text {
    font-family: "Barlow Condensed", "Arial Narrow", sans-serif;
    font-weight: 700;
    fill: var(--ink);
  }
  .wordmark-dot { fill: var(--accent-sky); }
  .site-scene {
    position: absolute;
    left: 0;
    bottom: 10px;
    width: 100%;
    height: 118px;
    background: linear-gradient(to bottom,
      var(--skyline-light) 0%,
      var(--skyline-mid) 55%,
      #a9acb1 80%,
      var(--silhouette) 100%);
  }
  .ground-line {
    position: absolute;
    left: 0;
    bottom: 0;
    width: 100%;
    height: 10px;
    background: var(--ground);
  }
</style>
</head>
<body>
  <main class="billboard">
    <div class="flag-band" aria-hidden="true">
      <div class="stripe-blue"></div>
      <div class="stripe-yellow"></div>
      <div class="stripe-red"></div>
    </div>

    <svg class="wordmark" viewBox="0 0 1200 260" role="heading" aria-level="1" aria-label="Vextra Civil">
      <circle class="wordmark-dot" cx="108" cy="160" r="78"/>
      <text class="wordmark-text" x="206" y="236" font-size="218" textLength="962" lengthAdjust="spacingAndGlyphs">VEXTRA CIVIL</text>
    </svg>

    <div class="site-scene" role="img" aria-label="Silhouettes of road works: roller, dump truck, workers, excavator and traffic cones in front of a grey city skyline with cranes"></div>
    <div class="ground-line" aria-hidden="true"></div>
  </main>
</body>
</html>
```